promotional flyer for Valtera Gym

we are after a double sided a5 leaflet to promote our gym, this is to go out to the general public to entice them into getting membership.

gym membership is £30 per month

it should also include the offer of - if you present this leaflet then there will be no joining fee

some of the features of the gym include

strength machines
cardio machines
functional area
sprung floor mat area

Target Market(s)

Adults 16+ who want to go to the gym and workout

Industry/Entity Type

Gym

Font styles to use
Other font styles liked:
• montserrat Regular

Requirements
Must have
• Clean on brand design
• use images supplied by us
Nice to have
• focus on an inclusive experience as the gym will be advertised to everyone
• should also use our "fitter, stronger, Healthier"

```html
<!DOCTYPE html>
<html lang="en">
<head>
<meta charset="utf-8">
<title>Valtera Gym – Membership Leaflet</title>
<link rel="stylesheet" href="https://fonts.googleapis.com/css2?family=Montserrat:wght@300;400;500;600;700;800&display=swap">
<style>
  :root{
    --backdrop:#333333;
    --slate:#515a62;
    --orange:#f15a29;
    --black:#000000;
    --white:#ffffff;
    --paper:#f7f7f7;
    --photo-dark:#2a2224;
    --photo-warm:#8a3a22;
  }
  *{box-sizing:border-box;margin:0;padding:0}
  html,body{width:1200px;height:1200px;overflow:hidden;background:var(--backdrop);font-family:"Montserrat",sans-serif;color:var(--white)}
  .leaflet{position:absolute;top:247px;width:530px;height:743px;overflow:hidden;box-shadow:0 8px 22px rgba(0,0,0,.45)}
  .leaflet--front{left:60px;background:var(--slate)}
  .leaflet--back{left:624px;background:var(--slate)}
  .abs{position:absolute}

  /* front */
  .front-photo{left:0;top:0;width:530px;height:422px;background:linear-gradient(135deg,#5a2a3a 0%,var(--photo-dark) 35%,var(--photo-warm) 70%,#3a2220 100%)}
  .brand-panel{left:0;top:0;width:320px;height:112px}
  .brand-name{left:0;width:260px;top:64px;text-align:center;font-size:17px;font-weight:400;letter-spacing:1.5px;color:var(--slate)}
  .motto-band{left:0;top:422px;width:530px;height:49px;background:var(--slate);font-size:28px;font-weight:500;text-align:center;line-height:49px;letter-spacing:.3px}
  .join-black{left:0;top:474px;width:274px;height:220px;background:var(--black);display:flex;flex-direction:column;justify-content:center;align-items:center;font-weight:800;font-size:37px;line-height:1.3}
  .join-black .wide{letter-spacing:4px;margin-right:-4px}
  .offer-orange{left:277px;top:474px;width:253px;height:220px;background:var(--orange);text-align:center}
  .offer-title{top:52px;left:0;width:253px;font-size:23.5px;font-weight:700}
  .offer-price{top:86px;left:0;width:253px;font-size:56px;font-weight:500;line-height:1}
  .offer-period{top:138px;left:47px;width:159px;height:30px;background:var(--black);font-size:29px;font-weight:500;line-height:31px}
  .offer-cta{top:176px;left:0;width:253px;font-size:29px;font-weight:300}
  .fee-band{left:0;top:698px;width:530px;height:45px;background:var(--slate);font-size:17px;font-weight:500;text-align:center;line-height:45px}
  .divider{background:var(--paper)}

  /* back */
  .back-photo{left:0;top:0;width:530px;height:354px;background:linear-gradient(160deg,#4a4f5a 0%,#2d2f36 40%,#7a5232 85%,#9b6a3e 100%)}
  .features-tag{left:0;top:370px;width:146px;height:29px;background:var(--orange);border-radius:0 15px 15px 0;font-size:22px;font-weight:500;line-height:29px;padding-left:21px}
  .feature{font-size:18px;font-weight:500;display:flex;align-items:center;gap:4px}
  .feature svg{width:13px;height:13px}
  .story{left:22px;top:484px;width:470px;font-size:12px;line-height:14.6px;font-weight:400}
  .contact-panel{left:0;top:602px;width:530px;height:141px;background:var(--orange)}
  .contact-tab{left:176px;top:586px;width:166px;height:40px;background:var(--black);font-size:21px;font-weight:500;text-align:center;line-height:42px}
  .contact-line{font-size:12px;font-weight:500;white-space:nowrap}
  .contact-line svg{width:12px;height:12px;vertical-align:-2px;margin-right:6px}
</style>
</head>
<body>

<section class="leaflet leaflet--front">
  <div class="abs front-photo" role="img" aria-label="Photo of a woman lifting dumbbells in the gym's weights area"></div>
  <svg class="abs brand-panel" viewBox="0 0 320 112" aria-hidden="true">
    <polygon points="252,0 266,0 222,112 208,112" fill="var(--slate)"/>
    <polygon points="0,0 252,0 208,112 0,112" fill="var(--white)"/>
  </svg>
  <div class="abs brand-name">VALTERA GYM</div>

  <div class="abs motto-band">FITTER | STRONGER | HEALTHIER</div>
  <div class="abs divider" style="left:0;top:471px;width:530px;height:3px"></div>

  <div class="abs join-black"><span class="wide">BECOME</span><span>A MEMBER</span></div>
  <div class="abs divider" style="left:274px;top:474px;width:3px;height:220px"></div>
  <div class="abs offer-orange">
    <div class="abs offer-title">Gym Membership</div>
    <div class="abs offer-price">£30</div>
    <div class="abs offer-period">Per Month</div>
    <div class="abs offer-cta">Join Us Today!</div>
  </div>
  <div class="abs divider" style="left:0;top:694px;width:530px;height:4px"></div>
  <div class="abs fee-band">If you present this leaflet then there will be no joining fee</div>
</section>

<section class="leaflet leaflet--back">
  <div class="abs back-photo" role="img" aria-label="Photo of two women riding spin bikes in the cardio studio"></div>
  <div class="abs features-tag">FEATURES</div>

  <div class="abs feature" style="left:34px;top:413px">
    <svg viewBox="0 0 13 13"><rect x="0.5" y="2.5" width="10" height="10" fill="none" stroke="#fff"/><path d="M2.5 7l3 3 6-9" fill="none" stroke="#fff" stroke-width="2"/></svg>Strength Machines</div>
  <div class="abs feature" style="left:277px;top:413px">
    <svg viewBox="0 0 13 13"><rect x="0.5" y="2.5" width="10" height="10" fill="none" stroke="#fff"/><path d="M2.5 7l3 3 6-9" fill="none" stroke="#fff" stroke-width="2"/></svg>Cardio Machines</div>
  <div class="abs feature" style="left:34px;top:442px">
    <svg viewBox="0 0 13 13"><rect x="0.5" y="2.5" width="10" height="10" fill="none" stroke="#fff"/><path d="M2.5 7l3 3 6-9" fill="none" stroke="#fff" stroke-width="2"/></svg>Functional Area</div>
  <div class="abs feature" style="left:277px;top:442px">
    <svg viewBox="0 0 13 13"><rect x="0.5" y="2.5" width="10" height="10" fill="none" stroke="#fff"/><path d="M2.5 7l3 3 6-9" fill="none" stroke="#fff" stroke-width="2"/></svg>Sprung Floor Mat Area</div>

  <p class="abs story">Valtera is the brainchild of medal winning Judo competitor Daniel Harwood and well-known fitness guru Leah Corran. Leah has been a personal trainer in the area for a number of years helping many clients achieve their goals, one of those clients was Daniel who was training for a big judo competition, after building a successful training partnership the pair began to pursue the dream of setting up Valtera, a name chosen to stand for strength.</p>

  <div class="abs contact-panel"></div>
  <svg class="abs" style="left:166px;top:586px" width="186" height="16" viewBox="0 0 186 16" aria-hidden="true">
    <polygon points="10,0 176,0 186,16 0,16" fill="var(--slate)"/>
  </svg>
  <div class="abs contact-tab">Contact Us</div>

  <div class="abs contact-line" style="left:26px;top:638px">Opening hours 6am - 10pm (Mon to Fri) and 7am to 7pm (Saturday and Sunday)</div>
  <div class="abs contact-line" style="left:28px;top:665px;display:flex;gap:0">
    <svg viewBox="0 0 12 16" style="width:12px;height:15px;margin-right:9px"><path d="M6 0a5.5 5.5 0 0 0-5.5 5.5C.5 10 6 16 6 16s5.5-6 5.5-10.5A5.5 5.5 0 0 0 6 0zm0 8a2.3 2.3 0 1 1 0-4.6A2.3 2.3 0 0 1 6 8z" fill="#fff"/></svg>
    <span>Unit 4 Kestrel Court, Marlow Road, Elmsworth,<br>West Sussex, BN99 7QX</span>
  </div>
  <div class="abs contact-line" style="left:24px;top:709px">
    <svg viewBox="0 0 12 12"><circle cx="6" cy="6" r="5.3" fill="none" stroke="#fff"/><path d="M4 3.2l1 1.6-.7.8c.5 1 1.1 1.6 2 2l.8-.7 1.6 1-.6 1.1C5.8 9 3 6.2 3 3.8z" fill="#fff"/></svg>01632 960418
    <svg viewBox="0 0 12 12" style="margin-left:8px"><rect x="1" y="3" width="10" height="7" fill="#fff"/><path d="M1 3l5 4 5-4" fill="none" stroke="var(--orange)"/></svg>hello@valteragym.co.uk
    <svg viewBox="0 0 12 12" style="margin-left:8px"><circle cx="6" cy="6" r="5" fill="none" stroke="#fff"/><ellipse cx="6" cy="6" rx="2.2" ry="5" fill="none" stroke="#fff"/><path d="M1 6h10" stroke="#fff"/></svg>www.valteragym.co.uk
  </div>
</section>

</body>
</html>
```